Artificial intelligence, machine learning, and automation company needs a sexy business card design

We need a sleek and sexy business card design for an AI consulting company based in Philadelphia PA. We provide custom machine learning and automation solutions for companies of all shapes and sizes. The primary industries that we serve are pharmaceuticals, engineering, healthcare, and computer software. We would like the designs to be a black business card that uses green as a sleek accent color. The final design should communicate intelligence, cutting edge new-tech, and optimization.

Target Market(s)

C-level and VP level executives of multi-million annual companies. Mostly in Pharma, Healthcare, Real Estate, Retail, and Engineering

Industry/Entity Type

Computer Software

Contact Information for Business Card

Name: Jack Moss
Title: CEO
Cell: 215 604 8293
Email: JackM@quillarcworks.example
Website: www.QuillarcWorks.example

Font styles to use
Sans Serif

Colors

Designer to choose colors to be used in the design.

Requirements
Must have
• 1) Attached Quillarc Logo (either with colors or not/embossed)
• 2) "Artificial Intelligence" "Automation" and "Machine Learning"
• 3) "Quillarc Laboratories" or "Quillarc Works" or "Quillarc"
• 4) Sexy AF.
Nice to have
• Black card / dark card color, "Quillarc Green" accent colors (in attached .ai file), Embossment of logo/name/etc, thick card stock, colored borders (on card sides, not front/back faces)
Should not have
• Should not be bland, or unsexy.

```html
<!DOCTYPE html>
<html lang="en">
<head>
<meta charset="utf-8">
<title>Quillarc Laboratories — Business Card</title>
<link rel="stylesheet" href="https://fonts.googleapis.com/css2?family=Oswald:wght@500&family=Lato:wght@400;700&family=Questrial&display=swap">
<style>
  :root {
    --backdrop: #2a201b;
    --card-front: #141414;
    --card-back: #2a2a2a;
    --accent: #3cc3ad;
    --silver: #8c8c8c;
    --silver-soft: #6e6e6e;
    --ink-light: #e8e8e8;
  }
  * { margin: 0; padding: 0; box-sizing: border-box; }
  html, body {
    width: 1200px; height: 715px; overflow: hidden;
    background: var(--backdrop);
  }
  .canvas {
    position: relative; width: 1200px; height: 715px;
    display: flex; align-items: center; justify-content: center; gap: 40px;
  }
  .card {
    position: relative; width: 540px; height: 309px;
    box-shadow: 0 14px 30px rgba(0,0,0,.45);
  }
  .card--front { background: var(--card-front); }
  .card--back { background: var(--card-back); }

  .brand {
    position: absolute; left: 78px; top: 100px;
    display: flex; align-items: center; gap: 16px;
  }
  .brand__square {
    width: 56px; height: 56px; border: 3px solid var(--silver);
  }
  .brand__name {
    font-family: "Questrial", sans-serif; color: var(--silver);
    line-height: 1.05; text-transform: uppercase;
  }
  .brand__name .line-1 { display: block; font-size: 40px; letter-spacing: 12px; }
  .brand__name .line-2 { display: block; font-size: 19px; letter-spacing: 6px; }
  .tagline {
    position: absolute; left: 78px; top: 200px;
    font-family: "Questrial", sans-serif; font-size: 15px;
    color: var(--silver-soft);
  }

  .person { position: absolute; left: 40px; top: 42px; }
  .person__name {
    font-family: "Oswald", sans-serif; font-weight: 500; font-size: 22px;
    color: var(--accent); text-transform: uppercase; letter-spacing: .5px;
  }
  .person__title {
    font-family: "Lato", sans-serif; font-size: 10px; color: var(--ink-light);
    margin-left: 4px; text-transform: uppercase;
  }
  .person__web {
    font-family: "Lato", sans-serif; font-weight: 700; font-size: 13px;
    color: var(--accent); margin-top: 2px;
  }
  .contact {
    position: absolute; left: 40px; top: 210px; list-style: none;
    font-family: "Lato", sans-serif; font-size: 12px; color: var(--ink-light);
  }
  .contact li { display: flex; align-items: center; gap: 10px; margin-bottom: 6px; }
  .contact svg { width: 11px; height: 11px; fill: var(--ink-light); }
  .mark {
    position: absolute; right: 40px; top: 118px;
    display: flex; align-items: center; gap: 12px;
  }
  .mark__square { width: 26px; height: 26px; border: 3px solid var(--accent); }
  .mark__name {
    font-family: "Lato", sans-serif; font-weight: 700; font-size: 20px;
    color: var(--accent); text-transform: uppercase; letter-spacing: 2px;
  }
</style>
</head>
<body>
<main class="canvas">
  <section class="card card--front" aria-label="Card front">
    <div class="brand">
      <div class="brand__square"></div>
      <p class="brand__name"><span class="line-1">Quillarc</span><span class="line-2">Laboratories</span></p>
    </div>
    <p class="tagline">Artificial Intelligence, Automation and Machine Learning</p>
  </section>

  <section class="card card--back" aria-label="Card back">
    <div class="person">
      <p><span class="person__name">Jack Moss</span><span class="person__title">CEO</span></p>
      <p class="person__web">www.QuillarcWorks.example</p>
    </div>
    <ul class="contact">
      <li>
        <svg viewBox="0 0 24 24" aria-hidden="true"><path d="M6.6 10.8a15.1 15.1 0 0 0 6.6 6.6l2.2-2.2a1 1 0 0 1 1-.25 11.4 11.4 0 0 0 3.6.57 1 1 0 0 1 1 1V20a1 1 0 0 1-1 1A17 17 0 0 1 3 4a1 1 0 0 1 1-1h3.5a1 1 0 0 1 1 1c0 1.25.2 2.45.57 3.57a1 1 0 0 1-.25 1z"/></svg>
        215 604 8293
      </li>
      <li>
        <svg viewBox="0 0 24 24" aria-hidden="true"><path d="M2 5h20v14H2zm2 2v.5l8 5 8-5V7l-8 5z"/></svg>
        JackM@quillarcworks.example
      </li>
    </ul>
    <div class="mark">
      <div class="mark__square"></div>
      <span class="mark__name">Quillarc</span>
    </div>
  </section>
</main>
</body>
</html>
```